Gelato Business Card

create a new business card using existing logo

Target Market(s)

B2B

Contact Information for Business Card

typical contact info: logo, address, email, phone, rep name

Colors
0355a3
33a6d7

Requirements
Must have
• a feel of high quality, luxury, happiness
• use cool, comforting color and texture of business card.
Nice to have
• "Every Scoop Made With Care!" TM
• or, "more quality, more flavor"
• or, "Flavor Matters"

```html
<!DOCTYPE html>
<html lang="en">
<head>
<meta charset="utf-8">
<title>Venelli's Artisan Gelato – Business Card</title>
<link href="https://fonts.googleapis.com/css2?family=Montserrat:wght@500;700;800&family=Open+Sans:wght@400;600&display=swap" rel="stylesheet">
<style>
  :root {
    --brand-blue: #0355a3;
    --brand-cyan: #33a6d7;
    --brand-indigo: #3a3fa8;
    --card-grey: #e0e0e1;
    --ink: #1e1e24;
    --rule: #9a9a9e;
    --stage: #3a3a3d;
    --white: #ffffff;
  }
  * { box-sizing: border-box; margin: 0; padding: 0; }
  html, body { width: 1200px; height: 896px; overflow: hidden; }
  body {
    background: var(--stage);
    display: flex; flex-direction: column; align-items: center; justify-content: center;
    gap: 48px;
    font-family: "Open Sans", Arial, sans-serif;
  }
  .card {
    position: relative; width: 640px; height: 366px; overflow: hidden;
    box-shadow: 0 10px 28px rgba(0,0,0,.45);
  }

  /* Front */
  .card-front { background: var(--card-grey); }
  .front-watermark {
    position: absolute; left: 150px; top: -30px; width: 250px; height: 190px;
    border-radius: 50%;
    background: radial-gradient(ellipse at center, rgba(160,160,165,.35), rgba(224,224,225,0) 70%);
  }
  .front-rule {
    position: absolute; left: 0; top: 0; width: 640px; height: 366px;
  }
  .contact-block { position: absolute; left: 46px; top: 104px; }
  .rep-name {
    font-family: "Montserrat", Arial, sans-serif; font-weight: 700;
    font-size: 24px; color: var(--brand-indigo); letter-spacing: .5px; text-transform: uppercase;
  }
  .rep-title { font-size: 15px; color: var(--ink); margin-top: 2px; margin-bottom: 14px; }
  .contact-line { display: flex; align-items: center; gap: 8px; font-size: 15px; color: var(--ink); line-height: 22px; }
  .contact-line svg { width: 14px; height: 14px; fill: var(--brand-indigo); flex: none; }
  .front-brand {
    position: absolute; right: 52px; top: 128px; text-align: center;
    font-family: "Montserrat", Arial, sans-serif; font-weight: 800;
    color: var(--brand-indigo);
  }
  .front-brand .brand-name { font-size: 40px; line-height: 1; }
  .front-brand .brand-sub { font-size: 12px; letter-spacing: 4px; margin-top: 6px; }
  .address {
    position: absolute; right: 46px; bottom: 54px; text-align: right;
    font-size: 16px; color: var(--ink); line-height: 22px;
  }

  /* Back */
  .card-back {
    background: linear-gradient(200deg, var(--brand-cyan) 0%, var(--brand-blue) 55%, var(--brand-indigo) 100%);
    display: flex; flex-direction: column; align-items: center; justify-content: center;
    color: var(--white);
  }
  .back-watermark {
    position: absolute; left: 40px; top: 40px; width: 300px; height: 300px; border-radius: 50%;
    background: radial-gradient(ellipse at center, rgba(255,255,255,.14), rgba(255,255,255,0) 70%);
  }
  .back-brand { position: relative; text-align: center; font-family: "Montserrat", Arial, sans-serif; font-weight: 800; }
  .back-brand .brand-name { font-size: 52px; line-height: 1; }
  .back-brand .brand-sub { font-size: 14px; letter-spacing: 5px; margin-top: 8px; }
  .tagline {
    position: relative; margin-top: 40px;
    font-family: "Montserrat", Arial, sans-serif; font-weight: 700;
    font-size: 17px; letter-spacing: 1px; text-transform: uppercase;
  }
</style>
</head>
<body>

<section class="card card-front">
  <div class="front-watermark" role="img" aria-label="Faint brand symbol decoration"></div>
  <svg class="front-rule" viewBox="0 0 640 366" aria-hidden="true">
    <defs>
      <linearGradient id="bandGrad" x1="0" x2="1" y1="0" y2="0">
        <stop offset="0" stop-color="#3a3fa8"/>
        <stop offset="0.45" stop-color="#0355a3"/>
        <stop offset="1" stop-color="#33a6d7"/>
      </linearGradient>
    </defs>
    <line x1="20" y1="262" x2="620" y2="262" stroke="#9a9a9e" stroke-width="1"/>
    <polygon points="0,350 640,350 640,366 0,366" fill="url(#bandGrad)"/>
  </svg>

  <div class="contact-block">
    <div class="rep-name">Marcus Vale</div>
    <div class="rep-title">Managing Director</div>
    <div class="contact-line">
      <svg viewBox="0 0 16 16"><path d="M3 1h3l1 4-2 1a9 9 0 0 0 5 5l1-2 4 1v3a2 2 0 0 1-2 2A13 13 0 0 1 1 3a2 2 0 0 1 2-2z"/></svg>
      021-555 204 118
    </div>
    <div class="contact-line">
      <svg viewBox="0 0 16 16"><path d="M4 0h8a1 1 0 0 1 1 1v14a1 1 0 0 1-1 1H4a1 1 0 0 1-1-1V1a1 1 0 0 1 1-1zm1 2v10h6V2zm3 11a1 1 0 1 0 0 2 1 1 0 0 0 0-2z"/></svg>
      021-555 204 118
    </div>
    <div class="contact-line">
      <svg viewBox="0 0 16 16"><path d="M0 3h16v10H0zm1 1v.5l7 5 7-5V4zm0 2v6h14V6l-7 5z"/></svg>
      hello@venelligelato.com
    </div>
  </div>

  <div class="front-brand">
    <div class="brand-name">Venelli's</div>
    <div class="brand-sub">ARTISAN GELATO</div>
  </div>

  <div class="address">
    48 Harbour Lane,<br>Brightwater, 204118
  </div>
</section>

<section class="card card-back">
  <div class="back-watermark" role="img" aria-label="Faint brand symbol decoration"></div>
  <div class="back-brand">
    <div class="brand-name">Venelli's</div>
    <div class="brand-sub">ARTISAN GELATO</div>
  </div>
  <div class="tagline">Every Scoop Made With Care!</div>
</section>

</body>
</html>
```